Large footwear retailer needs new powerpoint template

We are an Australian footwear retailer - Wombledge Footwear that needs a new powerpoint template. We want it to be fun and using our brand colours Teal and Black.
This will be used for multiple presentations so should include title slides, slides that allow us to high light our digital execution's, graphs, overviews and detail.
It can be bold and playful but also easy to use.
our website: https://www.wombledgefootwear.example.au/
Our Instagram: https://www.instagram.com/wombledge_kicks/

```html
<!DOCTYPE html>
<html lang="en">
<head>
<meta charset="utf-8">
<title>Wombledge Footwear – Presentation Template</title>
<link href="https://fonts.googleapis.com/css2?family=Poppins:wght@400;500;600;700;800&display=swap" rel="stylesheet">
<style>
:root{
  --board:#8e8e8e;
  --teal:#2bb5b1;
  --teal-soft:#5fbdb5;
  --teal-pale:#dcf1ef;
  --cyan:#0fe0de;
  --ink:#0c0c0c;
  --ink-dark:#263a38;
  --grey-slice:#5f5f5f;
  --text:#4a4a4a;
  --card:#e6e6e8;
  --star:#e7a21b;
  --white:#ffffff;
}
*{box-sizing:border-box;margin:0;padding:0}
html,body{width:1200px;height:1073px;overflow:hidden;background:var(--board)}
body{position:relative;font-family:"Poppins",sans-serif;color:var(--ink)}
.slide{position:absolute;width:481px;height:271px;background:var(--white);overflow:hidden}
.col-a{left:103px}.col-b{left:616px}
.row-1{top:99px}.row-2{top:405px}.row-3{top:704px}
.abs{position:absolute}
.brand{position:absolute;left:10px;top:10px;display:flex;align-items:center;gap:2px;font-weight:800;font-size:10px;letter-spacing:.1px;color:var(--ink)}
.brand-dot{width:9px;height:9px;border-radius:50%;background:var(--teal)}
.teal{color:var(--teal)}
.stars{color:var(--star);letter-spacing:1px}
.body-copy{font-size:6.5px;line-height:10.3px;color:var(--text);text-align:justify}

/* title slide */
.title-slide{background:linear-gradient(90deg,#e9f6f5 0%,#d2eeeb 45%,var(--teal-soft) 72%,var(--teal-soft) 100%)}
.title-slide .headline{left:56px;top:56px;font-weight:800;font-size:28px;line-height:34px;color:var(--ink)}
.title-slide .headline .teal{color:var(--teal-soft)}
.title-slide .lead{left:56px;top:168px;width:190px;font-size:7.5px;line-height:11.5px;color:var(--text)}
.hero-photo{left:263px;top:39px;width:170px;height:170px;border-radius:50%;background:radial-gradient(circle at 45% 45%,#f2f4f5 0%,#c9d2d6 50%,#8fb6b4 100%)}

/* collection slide */
.side-band{left:0;top:0;width:51px;height:271px;background:var(--teal)}
.side-label{left:25px;top:145px;transform:translate(-50%,-50%) rotate(-90deg);white-space:nowrap;color:var(--white);font-weight:800;font-size:13.5px;letter-spacing:.2px}
.collection .stars{left:0;width:481px;top:23px;text-align:center;font-size:7px}
.collection h2{position:absolute;left:51px;right:0;top:36px;text-align:center;font-weight:800;font-size:14px}
.collection .intro{left:70px;width:342px;top:60px;font-size:6.5px;line-height:10.2px;color:var(--text);text-align:center}
.product{position:absolute;top:103px;width:94px}
.product-shot{height:100px;background:linear-gradient(180deg,#ececee,#dedee0);border-radius:2px}
.product .maker{margin-top:4px;font-size:5.5px;font-weight:600;color:var(--teal)}
.product .name{font-size:5.8px;color:var(--ink);line-height:8px}
.product .stars{position:static;font-size:5px;text-align:left}
.product .price{font-size:6px;font-weight:600;color:var(--teal)}

/* product detail */
.gallery-main{left:9px;top:34px;width:207px;height:185px;background:radial-gradient(ellipse at 50% 55%,#f6f6f6 0%,#e4e4e6 60%)}
.thumb{position:absolute;top:223px;width:32px;height:27px;background:#e8e8ea}
.thumb.more{background:#a8dcd8;font-size:7px;font-weight:500;display:flex;align-items:center;justify-content:center;color:var(--ink)}
.maker-mark{left:235px;top:34px;font-size:8px;font-weight:800;color:var(--ink)}
.detail h3{position:absolute;left:235px;top:54px;font-size:11px;font-weight:700}
.detail .desc{left:235px;top:71px;width:200px;font-size:4.6px;line-height:7.4px;color:var(--ink);text-align:justify}
.detail .stars{left:235px;top:101px;font-size:6px}
.spec{position:absolute;left:235px;font-size:5.5px;color:var(--text)}
.spec b{color:var(--ink);font-weight:600}
.swatch{position:absolute;top:138px;width:11px;height:11px;border-radius:50%;background:#e6e6e6}
.size-box{position:absolute;top:172px;width:13px;height:11px;border:.6px solid #bdbdbd;font-size:4.5px;color:var(--text);display:flex;align-items:center;justify-content:center}
.qty{position:absolute;left:234px;top:195px;display:flex;align-items:center;gap:5px;font-size:7px;font-weight:600}
.qty span.c{width:8px;height:8px;border:.7px solid var(--ink);border-radius:50%;font-size:6px;line-height:6.5px;text-align:center;font-weight:500}
.details-bar{left:231px;top:215px;width:232px;height:19px;background:#eceff0;display:flex;align-items:center;justify-content:space-between;padding:0 8px;font-size:7px;font-weight:600;color:var(--text)}

/* chart slide */
.chart{left:33px;top:47px}
.divider{left:236px;top:49px;width:1.3px;height:177px;background:var(--ink)}
.split-title{position:absolute;font-weight:800;font-size:14px;white-space:nowrap}
.chart-slide .split-title{left:259px;top:38px}
.chart-slide .body-copy{left:259px;width:189px}

/* about slide */
.about .split-title{left:18px;line-height:19px;font-size:14.5px}
.about .body-copy{left:18px;top:114px;width:189px}
.ring{left:252px;top:42px;width:204px;height:204px;border:.7px solid #777;border-radius:50%}
.about-photo{left:264px;top:54px;width:180px;height:180px;border-radius:50%;background:radial-gradient(circle at 55% 55%,#e9ecea 0%,#8fb7b0 45%,#5f5a7a 100%)}
.about-badge{left:376px;top:35px;width:56px;height:56px;border-radius:50%;background:var(--teal);color:var(--white);font-weight:700;font-size:10px;line-height:12px;display:flex;align-items:center;justify-content:center;text-align:center}

/* closing slide */
.closing-photo{left:0;top:0;width:370px;height:271px;background:linear-gradient(110deg,#9aa4a8 0%,#b8b6b0 25%,#f08a2e 45%,#f4963f 65%,#c9c3bb 100%)}
.closing-band{left:370px;top:0;width:111px;height:271px;background:var(--teal)}
.contact-card{left:272px;top:37px;width:143px;height:193px;background:var(--white)}
.contact-card .brand{left:15px;top:20px;font-size:14px}
.contact-card .brand-dot{width:12px;height:12px}
.contact-card h4{position:absolute;left:15px;top:50px;font-size:14px;font-weight:800}
.contact-card .note{left:15px;top:72px;width:118px;font-size:4.4px;line-height:7.6px;color:var(--ink)}
.contact-row{position:absolute;left:15px;display:flex;align-items:center;gap:6px;font-size:6.5px;color:var(--ink);line-height:8px}
.contact-row svg{flex:none}
.socials{position:absolute;left:15px;top:170px;display:flex;gap:7px}
.socials span{width:10px;height:10px;border-radius:50%;background:var(--teal)}
</style>
</head>
<body>

<!-- Title slide -->
<section class="slide col-a row-1 title-slide">
  <div class="brand">WOMBLEDGE<span class="brand-dot"></span></div>
  <div class="abs headline"><span class="teal">TAKE</span>&nbsp; YOUR<br>KICKS TO NEW<br><span class="teal">HEIGHTS</span></div>
  <p class="abs lead">Lorem ipsum dolor sit amet, consectetur adipiscing elit, sed do eiusmod tempor incididunt ut labore et dolore magna aliqua.</p>
  <div class="abs hero-photo" role="img" aria-label="Close-up photo of a white sneaker on a foot"></div>
</section>

<!-- New collection slide -->
<section class="slide col-b row-1 collection">
  <div class="abs side-band"></div>
  <div class="abs side-label">OUR DIGITAL EXECUTIONS</div>
  <div class="brand">WOMBLEDGE<span class="brand-dot"></span></div>
  <div class="abs stars">★★★★★</div>
  <h2>NEW <span class="teal">COLLECTION</span></h2>
  <p class="abs intro">Lorem ipsum dolor sit amet, consectetur adipiscing elit, sed do eiusmod tempor incididunt ut labore et dolore magna aliqua. Ut enim ad minim veniam, quis nostrud exercitation ullamco ex ea commodo consequat</p>
  <div class="product" style="left:61px">
    <div class="product-shot" role="img" aria-label="Cream sneaker with mustard accents"></div>
    <div class="maker">STRIDERA</div><div class="name">womens Aero Lite Sc</div>
    <div class="stars">★★★★★</div><div class="price">$120.00</div>
  </div>
  <div class="product" style="left:167px">
    <div class="product-shot" role="img" aria-label="White sneaker with orange sole and blue accents"></div>
    <div class="maker">STRIDERA</div><div class="name">Womens Aero Lite Pulse</div>
    <div class="stars">★★★★★</div><div class="price">$160.00</div>
  </div>
  <div class="product" style="left:273px">
    <div class="product-shot" role="img" aria-label="Black sneaker with white sole"></div>
    <div class="maker">STRIDERA</div><div class="name">Mens Aero Lite Pulse</div>
    <div class="stars">★★★★★</div><div class="price">$160.00</div>
  </div>
  <div class="product" style="left:379px">
    <div class="product-shot" role="img" aria-label="White court sneaker with black stripe"></div>
    <div class="maker">STRIDERA</div><div class="name">Womens Court Classic Lift</div>
    <div class="stars">★★★★★</div><div class="price">$130.00</div>
  </div>
</section>

<!-- Product detail slide -->
<section class="slide col-a row-2 detail">
  <div class="brand">WOMBLEDGE<span class="brand-dot"></span></div>
  <div class="abs gallery-main" role="img" aria-label="White court sneaker, side view"></div>
  <div class="thumb" style="left:9px" role="img" aria-label="Sneaker thumbnail"></div>
  <div class="thumb" style="left:44px" role="img" aria-label="Sneaker thumbnail"></div>
  <div class="thumb" style="left:79px" role="img" aria-label="Sneaker thumbnail"></div>
  <div class="thumb" style="left:114px" role="img" aria-label="Sneaker thumbnail"></div>
  <div class="thumb" style="left:149px" role="img" aria-label="Sneaker thumbnail"></div>
  <div class="thumb more" style="left:184px">+12</div>
  <div class="abs maker-mark">STRIDERA</div>
  <h3>Womens Court Classic Lift</h3>
  <p class="abs desc">Lorem ipsum dolor sit amet, consectetur adipiscing elit, sed do eiusmod tempor incididunt ut labore et dolore magna aliqua. Ut enim ad minim veniam, quis nostrud exercitation ullamco laboris nisi ut aliquip ex ea commodo consequat. Lorem ipsum dolor sit amet, consectetur adipiscing elit,</p>
  <div class="abs stars">★★★★★</div>
  <div class="spec" style="top:114px;font-size:6px"><b style="color:var(--text)">Price :</b> <b>$130.00</b></div>
  <div class="spec" style="top:125px;font-size:4.8px">Color : <b style="font-weight:500">WHITE/BLACK/HEMP/TEAM ORANGE</b></div>
  <div class="swatch" style="left:235px"></div>
  <div class="swatch" style="left:250px"></div>
  <div class="spec" style="top:152px;font-size:4.8px">Choose Size: <b style="font-weight:500">UK ▾</b></div>
  <div class="spec" style="left:312px;top:152px;font-size:4.8px">Size Chart</div>
  <div class="spec" style="top:163px;font-size:4.8px">Size</div>
  <div class="size-box" style="left:234px">2.5</div>
  <div class="size-box" style="left:254px">3.5</div>
  <div class="size-box" style="left:275px">4.5</div>
  <div class="size-box" style="left:295px">5.5</div>
  <div class="size-box" style="left:316px">6.5</div>
  <div class="size-box" style="left:336px">7.5</div>
  <div class="size-box" style="left:357px">8.5</div>
  <div class="size-box" style="left:377px">9.5</div>
  <div class="qty"><span class="c">−</span>1<span class="c">+</span></div>
  <div class="abs details-bar"><span>Details</span><span style="color:var(--ink)">+</span></div>
</section>

<!-- Chart slide -->
<section class="slide col-b row-2 chart-slide">
  <div class="brand">WOMBLEDGE<span class="brand-dot"></span></div>
  <svg class="abs chart" width="180" height="180" viewBox="33 47 180 180" role="img" aria-label="Pie chart: 30%, 10%, 35% and 25%">
    <circle cx="123" cy="137" r="90" fill="var(--teal-pale)"/>
    <path d="M123 137 L123 62 A75 75 0 1 1 67.6 187.6 Z" fill="var(--teal)" stroke="#fff" stroke-width=".8"/>
    <path d="M123 137 L67.6 187.6 A75 75 0 0 1 48.1 132.3 Z" fill="var(--ink-dark)" stroke="#fff" stroke-width=".8"/>
    <path d="M123 137 L48.1 132.3 A75 75 0 0 1 67.6 86.5 Z" fill="var(--cyan)" stroke="#fff" stroke-width=".8"/>
    <path d="M123 137 L67.6 86.5 A75 75 0 0 1 123 62 Z" fill="var(--grey-slice)" stroke="#fff" stroke-width=".8"/>
    <g fill="#fff" font-family="Poppins, sans-serif" font-size="9" text-anchor="middle">
      <text x="100" y="96">25%</text>
      <text x="77" y="123">35%</text>
      <text x="79" y="151">10%</text>
      <text x="154" y="141">30%</text>
    </g>
  </svg>
  <div class="abs divider"></div>
  <h2 class="split-title"><span class="teal">LOREM IPSUM</span> DOLOR SIT</h2>
  <p class="abs body-copy" style="top:66px">Lorem ipsum dolor sit amet, consectetur adipiscing elit, sed do eiusmod tempor incididunt ut labore et dolore magna aliqua. Ut enim ad minim veniam, quis nostrud exercitation ullamco laboris nisi ut aliquip ex ea commodo consequat. Lorem ipsum dolor sit amet, consectetur adipiscing elit, sed do eiusmod tempor incididunt ut labore et dolore magna aliqua. Ut enim ad minim veniam, quis nostrud exercitation ullamco laboris nisi ut aliquip ex ea commodo consequat.</p>
  <p class="abs body-copy" style="top:161px">Quis nostrud exercitation ullamco laboris nisi ut aliquip ex ea commodo consequat. Lorem ipsum dolor sit amet, consectetur adipiscing elit, sed do eiusmod tempor incididunt ut labore et dolore magna aliqua. Ut enim ad minim veniam, quis nostrud exercitation ullamco laboris nisi ut aliquip ex ea commodo consequat.</p>
</section>

<!-- About slide -->
<section class="slide col-a row-3 about">
  <div class="brand">WOMBLEDGE<span class="brand-dot"></span></div>
  <h2 class="split-title teal" style="top:74px">LOREM IPSUM DOLOR</h2>
  <h2 class="split-title" style="top:93px">SIT AMET, CONSECTETUR</h2>
  <p class="abs body-copy">Lorem ipsum dolor sit amet, consectetur adipiscing elit, sed do eiusmod tempor incididunt ut labore et dolore magna aliqua. Ut enim ad minim veniam, quis nostrud exercitation ullamco laboris nisi ut aliquip ex ea commodo consequat. Lorem ipsum dolor sit amet, consectetur adipiscing elit, sed do eiusmod tempor incididunt ut labore et dolore magna aliqua. Ut enim ad minim veniam, quis nostrud exercitation ullamco laboris nisi ut aliquip ex ea commodo consequat.</p>
  <div class="abs ring"></div>
  <div class="abs about-photo" role="img" aria-label="Hands lacing a white and teal sneaker"></div>
  <div class="abs about-badge">ABOUT<br>US</div>
</section>

<!-- Closing slide -->
<section class="slide col-b row-3 closing">
  <div class="abs closing-photo" role="img" aria-label="Young man in black hoodie sitting on an orange bench looking at his phone"></div>
  <div class="abs closing-band"></div>
  <div class="abs contact-card">
    <div class="brand">WOMBLEDGE<span class="brand-dot"></span></div>
    <h4><span class="teal">THANK</span> YOU</h4>
    <p class="abs note">Lorem ipsum dolor sit amet, consectetur adipiscing elit, sed do eiusmod tempor incididunt ut labore et dolore magna aliqua. Ut enim ad minim veniam,</p>
    <div class="contact-row" style="top:102px">
      <svg width="6" height="9" viewBox="0 0 6 9"><path d="M3 0a3 3 0 0 1 3 3c0 2.2-3 6-3 6S0 5.2 0 3a3 3 0 0 1 3-3z" fill="var(--teal)"/><circle cx="3" cy="3" r="1.1" fill="#fff"/></svg>
      <span>Lorem ipsum dolor sit amet,<br>adipiscing 2003</span>
    </div>
    <div class="contact-row" style="top:131px">
      <svg width="8" height="8" viewBox="0 0 8 8"><path d="M1.6 0l1.5 1.9-.8 1.2a5 5 0 0 0 2.6 2.6l1.2-.8L8 6.4 7 8C3 8 0 5 0 1z" fill="var(--teal)"/></svg>
      <span>+61 3 9000 0000</span>
    </div>
    <div class="contact-row" style="top:149px">
      <svg width="9" height="7" viewBox="0 0 9 7"><rect width="9" height="7" rx="1" fill="var(--teal)"/><path d="M0.5 1l4 3 4-3" stroke="#fff" stroke-width=".8" fill="none"/></svg>
      <span style="font-size:5.6px">info@wombledgefootwear.example.au</span>
    </div>
    <div class="socials"><span></span><span></span><span></span><span></span></div>
  </div>
</section>

</body>
</html>
```